Window and GutterCleaning Flyer A5 size double sided.

We need a double sided A5 flyer. Side 1, is for window cleaning, side 2 is for gutter cleaning. Licensed by Borough of Calderwick Authority.
Phone number 0800 471 3926.
Business address 17 Fenmarrow Loan, West Brankholm Edinburgh EH47 3TP.
www.bright-pane-services.example
We use a LoftOrb Gutter inspection Cam to view your gutters first to see if they need doing.
Window cleaning ; Professional window cleaning services, what we offer, water fed pole window cleaning able to reach windows up to 60 feet.
Conservatory cleaning.
Conservatory roof cleaning.
Fascias & Soffits cleaning.
Excellent Customer Service.
Target Market(s)
domestic houses
Industry/Entity Type
window cleaning
Look and feel
Each slider illustrates characteristics of the customer's brand and the style your logo design should communicate.

```html
<!DOCTYPE html>
<html lang="en">
<head>
<meta charset="utf-8">
<title>Bright Pane Services – Window &amp; Gutter Cleaning Flyer</title>
<link href="https://fonts.googleapis.com/css2?family=Poppins:ital,wght@0,400;0,600;0,700;0,800;1,600;1,700;1,800;1,900&display=swap" rel="stylesheet">
<style>
  :root {
    --stage: #5b5c5e;
    --navy: #28286a;
    --blue: #1459b3;
    --sky: #8dbde9;
    --pale: #a9cdef;
    --ink: #141414;
    --green: #3b7b2f;
    --white: #ffffff;
    --gold: #d9a93a;
  }
  * { box-sizing: border-box; margin: 0; padding: 0; }
  html, body { width: 1200px; height: 918px; overflow: hidden; }
  body { background: var(--stage); font-family: "Poppins", Arial, sans-serif; position: relative; }

  .flyer { position: absolute; top: 76px; width: 540px; height: 765px; background: var(--white); overflow: hidden; box-shadow: 0 4px 14px rgba(0,0,0,.35); }
  .flyer--windows { left: 54px; }
  .flyer--gutters { left: 606px; }
  .backdrop { position: absolute; inset: 0; width: 540px; height: 765px; }
  .abs { position: absolute; }

  .headline { left: 24px; top: 132px; color: var(--white); font-weight: 900; font-style: italic; font-size: 39px; line-height: 32px; text-transform: uppercase; letter-spacing: -.5px; text-shadow: 1px 2px 3px rgba(0,0,0,.35); }
  .headline-rule { left: 24px; top: 270px; width: 166px; height: 3px; background: var(--white); }
  .intro { left: 24px; top: 282px; width: 275px; color: var(--white); font-style: italic; font-weight: 700; font-size: 13.4px; line-height: 17px; }

  .brand-box { background: var(--pale); color: var(--navy); font-weight: 800; text-transform: uppercase; text-align: center; display: flex; align-items: center; justify-content: center; font-size: 13px; line-height: 15px; }
  .flyer--windows .brand-box { left: 394px; top: 86px; width: 122px; height: 60px; }
  .flyer--gutters .brand-box { left: 382px; top: 622px; width: 122px; height: 60px; }

  .licence { right: 24px; top: 276px; text-align: right; }
  .licence-by { color: var(--navy); font-style: italic; font-weight: 600; font-size: 16px; line-height: 16px; padding-bottom: 4px; border-bottom: 1.5px solid var(--navy); }
  .licence-body { color: var(--white); font-style: italic; font-weight: 800; font-size: 19px; line-height: 20px; padding-top: 3px; }

  .badge { left: 178px; top: 380px; width: 108px; height: 108px; }
  .photo { background: linear-gradient(135deg, #cfe0ef, #6f8fb3); }

  .section-title { color: var(--blue); font-weight: 800; font-style: italic; font-size: 19px; line-height: 19px; }
  .body-text { color: var(--ink); font-size: 12.6px; line-height: 15.5px; }

  .offer-list { left: 24px; top: 624px; width: 272px; list-style: none; }
  .offer-list li { display: flex; align-items: center; gap: 8px; font-size: 13px; color: var(--ink); height: 23px; border-bottom: 1px solid #d5dbe6; }
  .offer-list li:last-child { border-bottom: none; }
  .offer-icon { width: 16px; height: 16px; border: 1.5px solid var(--blue); flex: none; }

  .reasons { list-style: none; font-size: 12px; line-height: 16.6px; color: var(--ink); }
  .reasons li::before { content: "• "; }

  .tagline-band { left: 0; top: 699px; width: 540px; height: 15px; background: linear-gradient(90deg, var(--blue), #2c6fc2 60%, #e6eef8); color: var(--white); font-style: italic; font-size: 10.4px; line-height: 15px; padding-left: 23px; }

  .contact { left: 23px; font-size: 9.6px; line-height: 13px; color: var(--blue); letter-spacing: -.1px; white-space: nowrap; }
  .contact div { display: flex; align-items: center; gap: 4px; }
  .contact svg { width: 9px; height: 9px; flex: none; }
  .phone { right: 22px; top: 725px; display: flex; align-items: center; gap: 10px; color: var(--white); font-weight: 800; font-size: 21px; }
  .phone svg { width: 16px; height: 16px; }

  .gutter-title { left: 24px; top: 222px; color: var(--blue); font-weight: 900; font-style: italic; font-size: 50px; line-height: 43px; text-transform: uppercase; letter-spacing: -.5px; }
  .gutter-sub { left: 24px; top: 310px; color: var(--sky); font-weight: 700; font-size: 25px; line-height: 26px; letter-spacing: .3px; }
  .gutter-desc { left: 24px; top: 337px; width: 300px; color: var(--ink); font-weight: 600; font-size: 12px; line-height: 14.5px; }

  .part-tag { height: 28px; }
  .part-tag text { font-family: "Poppins", Arial, sans-serif; font-weight: 600; font-size: 13px; fill: var(--white); }

  .cam-title { left: 387px; top: 406px; color: var(--white); font-weight: 800; font-style: italic; font-size: 23px; line-height: 27px; }

  .why-list { left: 24px; top: 596px; width: 240px; list-style: none; }
  .why-list li { position: relative; padding-left: 9px; border-bottom: 1px solid #bcc7de; padding-bottom: 2px; margin-bottom: 3px; }
  .why-list li::before { content: ""; position: absolute; left: 0; top: 4px; border-left: 5px solid var(--sky); border-top: 4px solid transparent; border-bottom: 4px solid transparent; }
  .why-list li:last-child { border-bottom: none; }
  .why-list strong { display: block; color: var(--navy); font-weight: 700; font-size: 11.5px; line-height: 14px; }
  .why-list span { display: block; color: #333; font-size: 11px; line-height: 13px; }
</style>
</head>
<body>

<!-- SIDE 1: WINDOW CLEANING -->
<section class="flyer flyer--windows">
  <svg class="backdrop" viewBox="0 0 540 765" aria-hidden="true">
    <defs>
      <linearGradient id="winPhoto" x1="0" y1="0" x2="1" y2="1">
        <stop offset="0" stop-color="#dce8f3"/>
        <stop offset=".45" stop-color="#2d74c4"/>
        <stop offset="1" stop-color="#1a58ad"/>
      </linearGradient>
    </defs>
    <polygon points="0,0 540,0 540,420 300,328 0,470" fill="url(#winPhoto)"/>
    <polygon points="0,82 110,122 0,165" fill="var(--navy)"/>
    <polygon points="0,300 540,153 540,195 300,328 0,470" fill="var(--navy)" opacity=".95"/>
    <polygon points="300,328 540,195 540,420" fill="var(--sky)"/>
    <polygon points="520,412 540,410 540,424" fill="var(--navy)"/>
    <polygon points="0,714 540,714 540,765 0,765" fill="var(--white)"/>
    <polygon points="239,765 351,714 540,714 540,765" fill="var(--navy)"/>
  </svg>
  <div class="abs" role="img" aria-label="Photo of a window cleaner washing a tall glass window with a squeegee" style="left:190px;top:0;width:230px;height:150px;"></div>

  <div class="abs brand-box">Bright Pane<br>Services</div>

  <h1 class="abs headline">Professional<br>Window<br>Cleaning<br>Services</h1>
  <div class="abs headline-rule"></div>
  <p class="abs intro">We offer high-quality window cleaning for homes and businesses, delivering. We only clean domestic properties not businesses.</p>

  <div class="abs licence">
    <div class="licence-by">Licensed<br>by Borough of</div>
    <div class="licence-body">Calderwick<br>Authority</div>
  </div>

  <svg class="abs badge" viewBox="0 0 108 108" role="img" aria-label="Satisfaction guarantee seal">
    <circle cx="54" cy="54" r="50" fill="var(--gold)"/>
    <circle cx="54" cy="54" r="36" fill="var(--white)"/>
  </svg>

  <div class="abs photo" role="img" aria-label="Water fed pole brush spraying a window" style="left:329px;top:366px;width:56px;height:109px;"></div>
  <div class="abs photo" role="img" aria-label="Brick house front with clean windows" style="left:387px;top:366px;width:45px;height:109px;background:linear-gradient(135deg,#b9694b,#e8e2d8);"></div>
  <div class="abs photo" role="img" aria-label="Pole cleaning an upper window frame" style="left:434px;top:366px;width:85px;height:109px;background:linear-gradient(135deg,#e8eef2,#8a9a8e);"></div>
  <div class="abs photo" role="img" aria-label="Conservatory roof half cleaned with moss on the panels" style="left:329px;top:488px;width:190px;height:113px;background:linear-gradient(160deg,#dfe5ea,#8f8f6a 60%,#c8ccd0);"></div>

  <h2 class="abs section-title" style="left:23px;top:492px;">Pure Water Fed<br>Pole System</h2>
  <p class="abs body-text" style="left:23px;top:532px;width:300px;">Our advanced system reaches up to 60 feet high, safely cleaning upper windows from the ground without the need for ladders.</p>

  <h2 class="abs section-title" style="left:23px;top:598px;">We Also Offer</h2>
  <ul class="abs offer-list">
    <li><span class="offer-icon"></span>Conservatory Window Cleaning</li>
    <li><span class="offer-icon"></span>Conservatory Roof Cleaning</li>
    <li><span class="offer-icon"></span>Fascia &amp; Soffit Cleaning</li>
  </ul>

  <h2 class="abs section-title" style="left:327px;top:610px;">Why Choose Us?</h2>
  <ul class="abs reasons" style="left:329px;top:629px;">
    <li>Friendly, professional service</li>
    <li>Reliable and efficient</li>
    <li>Fully licensed and insured</li>
    <li>Excellent customer satisfaction</li>
  </ul>

  <p class="abs tagline-band">spotless, streak-free results every time. As per last info, can't claim this too.</p>

  <div class="abs contact" style="top:723px;">
    <div><svg viewBox="0 0 10 10"><path d="M5 0a3.5 3.5 0 0 0-3.5 3.5C1.5 6 5 10 5 10s3.5-4 3.5-6.5A3.5 3.5 0 0 0 5 0zm0 5a1.4 1.4 0 1 1 0-2.8A1.4 1.4 0 0 1 5 5z" fill="var(--navy)"/></svg>17 Fenmarrow Loan, West Brankholm, Edinburgh EH47 3TP</div>
    <div><svg viewBox="0 0 10 10"><circle cx="5" cy="5" r="4.3" fill="none" stroke="var(--navy)" stroke-width="1.1"/><path d="M.7 5h8.6M5 .7c-2.2 2.4-2.2 6.2 0 8.6M5 .7c2.2 2.4 2.2 6.2 0 8.6" fill="none" stroke="var(--navy)" stroke-width=".9"/></svg>www.bright-pane-services.example</div>
  </div>
  <div class="abs phone">
    <svg viewBox="0 0 16 16"><path d="M3.6 1 6 3.6 4.6 5.4c.9 2 2.4 3.5 4.4 4.4l1.8-1.4L13.4 11l-1.6 2.8C6.6 13.4 2.6 9.4 1 3.4z" fill="var(--sky)"/></svg>
    0800 471 3926
  </div>
</section>

<!-- SIDE 2: GUTTER CLEANING -->
<section class="flyer flyer--gutters">
  <svg class="backdrop" viewBox="0 0 540 765" aria-hidden="true">
    <defs>
      <linearGradient id="gutPhoto" x1="0" y1="0" x2="1" y2="1">
        <stop offset="0" stop-color="#1d4fa8"/>
        <stop offset=".5" stop-color="#5f7ea8"/>
        <stop offset="1" stop-color="#8b7a6c"/>
      </linearGradient>
      <linearGradient id="sidePanel" x1="0" y1="0" x2="1" y2="1">
        <stop offset="0" stop-color="#2f6fc6"/>
        <stop offset="1" stop-color="#164fa6"/>
      </linearGradient>
    </defs>
    <rect width="540" height="310" fill="url(#gutPhoto)"/>
    <polygon points="0,158 169,76 540,229 540,320 169,153 0,224" fill="var(--navy)"/>
    <polygon points="0,224 169,153 540,310 540,765 0,765" fill="var(--white)"/>
    <polygon points="0,224 169,153 540,310 540,318 169,161 0,232" fill="var(--blue)"/>
    <polygon points="300,377 540,300 540,714 300,714" fill="url(#sidePanel)" opacity=".9"/>
    <polygon points="250,714 300,560 430,540 540,600 540,714" fill="#dfe7f1" opacity=".85"/>
    <polygon points="0,714 540,714 540,765 0,765" fill="var(--white)"/>
    <polygon points="239,765 351,714 540,714 540,765" fill="var(--navy)"/>
  </svg>
  <div class="abs" role="img" aria-label="Photo of a blue vacuum hose clearing moss from a roof gutter" style="left:300px;top:0;width:240px;height:300px;"></div>
  <div class="abs" role="img" aria-label="Handheld inspection camera screen showing a house, in front of a roofline with gutter and soffit" style="left:0;top:377px;width:400px;height:168px;background:linear-gradient(135deg,#cfd6de,#6e7884 55%,#2a2d33);"></div>

  <h1 class="abs gutter-title">Gutter<br>Cleaning</h1>
  <p class="abs gutter-sub">SAFE SMART CLEAN</p>
  <p class="abs gutter-desc">Our ground-based system safely clears moss, leaves, and debris no ladders required!</p>

  <svg class="abs part-tag" style="left:63px;top:392px;" width="88" height="28" viewBox="0 0 88 28" aria-label="Gutter">
    <polygon points="6,4 70,4 70,0 88,14 70,28 70,24 0,24" fill="var(--green)"/>
    <text x="14" y="19">Gutter</text>
  </svg>
  <svg class="abs part-tag" style="left:36px;top:438px;" width="88" height="28" viewBox="0 0 88 28" aria-label="Fascia">
    <polygon points="6,4 70,4 70,0 88,14 70,28 70,24 0,24" fill="var(--green)"/>
    <text x="14" y="19">Fascia</text>
  </svg>
  <svg class="abs part-tag" style="left:10px;top:490px;" width="88" height="28" viewBox="0 0 88 28" aria-label="Soffit">
    <polygon points="6,4 70,4 70,0 88,14 70,28 70,24 0,24" fill="var(--green)"/>
    <text x="14" y="19">Soffit</text>
  </svg>

  <p class="abs cam-title">LoftOrb®<br>Gutter<br>Inspection<br>Cam</p>

  <h2 class="abs section-title" style="left:24px;top:568px;font-size:21px;">Why Choose Us?</h2>
  <ul class="abs why-list">
    <li><strong>Camera Inspection First</strong><span>see exactly what needs cleaning</span></li>
    <li><strong>Safe &amp; Professional</strong><span>no damage, no disruption</span></li>
    <li><strong>Licensed &amp; Insured</strong></li>
    <li><strong>Free Quote – No Obligation</strong></li>
  </ul>

  <div class="abs brand-box">Bright Pane<br>Services</div>

  <div class="abs contact" style="top:723px;">
    <div><svg viewBox="0 0 10 10"><path d="M5 0a3.5 3.5 0 0 0-3.5 3.5C1.5 6 5 10 5 10s3.5-4 3.5-6.5A3.5 3.5 0 0 0 5 0zm0 5a1.4 1.4 0 1 1 0-2.8A1.4 1.4 0 0 1 5 5z" fill="var(--navy)"/></svg>17 Fenmarrow Loan, West Brankholm, Edinburgh EH47 3TP</div>
    <div><svg viewBox="0 0 10 10"><circle cx="5" cy="5" r="4.3" fill="none" stroke="var(--navy)" stroke-width="1.1"/><path d="M.7 5h8.6M5 .7c-2.2 2.4-2.2 6.2 0 8.6M5 .7c2.2 2.4 2.2 6.2 0 8.6" fill="none" stroke="var(--navy)" stroke-width=".9"/></svg>www.bright-pane-services.example</div>
  </div>
  <div class="abs phone">
    <svg viewBox="0 0 16 16"><path d="M3.6 1 6 3.6 4.6 5.4c.9 2 2.4 3.5 4.4 4.4l1.8-1.4L13.4 11l-1.6 2.8C6.6 13.4 2.6 9.4 1 3.4z" fill="var(--sky)"/></svg>
    0800 471 3926
  </div>
</section>

</body>
</html>
```